Meridale Eating needs Stationary and a business card

We would like to use our current logo. The text can be moved around as needed. The stationary needs to be a 'first page' where the logo is more prominent to be impressive on higher quality paper and a second page where the logo is more subtle where there will be much more information on the page. There are 2 clinic locations which will need include name, address, phone number, fax number, web address. The business card should be single sided and contain this information also.
The design must be contemporary and sophisticated as this is a science based diet run out of a medical clinic.

Target Market(s)

People wanting to lose weight, athletes looking to optimise performance, people with arthritis or fighting cancer

Industry/Entity Type

Business

Contact Information for Business Card

must use the logo. I have attached an example card with the practice details on it. there must be space for the doctors name. Also the website www.meridaleeating.example.au

Requirements
Must have
• the logo, the business adresses and phone numbers, the website, the doctors name and qualifications
Nice to have
• some creativity
Should not have
• Do not simply reproduce the existing card please

```html
<!DOCTYPE html>
<html lang="en">
<head>
<meta charset="utf-8">
<title>Meridale Eating — Stationery</title>
<link rel="stylesheet" href="https://fonts.googleapis.com/css2?family=Didact+Gothic&family=Mulish:wght@700;800&display=swap">
<style>
  :root{
    --bg:#cbcbcb;
    --paper:#ffffff;
    --card:#f7f7f7;
    --brand-blue:#1a8fd6;
    --brand-navy:#1e4f8f;
    --sky:#3cb4e6;
    --ink:#2a2a2a;
    --faint:#e3eef5;
  }
  *{box-sizing:border-box;margin:0;padding:0}
  html,body{width:1200px;height:1200px;overflow:hidden;background:var(--bg)}
  body{position:relative;font-family:"Didact Gothic",sans-serif;color:var(--ink)}

  .letterhead{position:absolute;left:305px;top:136px;width:666px;height:944px;background:var(--paper);overflow:hidden}
  .brand{position:absolute;display:flex;flex-direction:column;align-items:center}
  .brand__mark{border-radius:50%;background:var(--sky)}
  .brand__name{font-family:"Didact Gothic",sans-serif;color:var(--brand-navy);white-space:nowrap}
  .letterhead .brand{left:19px;top:30px;width:160px}
  .letterhead .brand__mark{width:82px;height:82px}
  .letterhead .brand__name{font-size:19px;margin-top:18px}

  .doctor{position:absolute;text-align:right}
  .doctor__name{font-family:"Mulish",sans-serif;font-weight:800;color:var(--ink)}
  .doctor__quals{color:var(--ink)}
  .doctor__role{color:var(--brand-blue)}
  .letterhead .doctor{right:32px;top:66px}
  .letterhead .doctor__name{font-size:17px;line-height:20px}
  .letterhead .doctor__quals{font-size:6px;line-height:9px;letter-spacing:.1px}
  .letterhead .doctor__role{font-size:10px;line-height:13px}

  .clinics{position:absolute;right:497px;top:184px;text-align:right;font-size:11.5px;line-height:13.4px;white-space:nowrap}
  .clinic{margin-bottom:15px}
  .clinic__place{color:var(--brand-blue)}
  .clinic__gap{height:6px}

  .watermark{position:absolute;left:327px;top:600px;width:360px;height:360px;border-radius:50%;background:var(--faint);opacity:.8}

  .card{position:absolute;width:291px;height:178px;background:var(--card);overflow:hidden}
  .card--details{left:197px;top:520px}
  .card--brand{left:197px;top:744px}
  .card--details .brand{left:6px;top:12px;width:108px}
  .card--details .brand__mark{width:48px;height:48px}
  .card--details .brand__name{font-size:11px;margin-top:10px}
  .card--details .doctor{right:13px;top:41px}
  .card--details .doctor__name{font-size:8.5px;line-height:10px}
  .card--details .doctor__quals{font-size:3.5px;line-height:5px}
  .card--details .doctor__role{font-size:7px;line-height:9px}
  .card__clinic{position:absolute;bottom:17px;font-size:7px;line-height:8.8px;white-space:nowrap}
  .card__clinic--left{left:10px}
  .card__clinic--right{right:10px;text-align:right}
  .card__clinic .clinic__gap{height:8px}
  .icon{display:inline-block;width:6px;height:6px;vertical-align:-0.5px}
  .card__rule{position:absolute;left:0;right:0;bottom:11px;height:2px;background:var(--brand-navy)}
  .card__band{position:absolute;left:0;right:0;bottom:0;height:9px;background:var(--sky)}

  .card--brand .brand{left:0;right:0;top:45px}
  .card--brand .brand__mark{width:64px;height:64px}
  .card--brand .brand__name{font-size:14px;margin-top:12px}
</style>
</head>
<body>

<section class="letterhead">
  <div class="watermark" aria-hidden="true"></div>
  <div class="brand">
    <div class="brand__mark"></div>
    <div class="brand__name">Meridale Eating</div>
  </div>
  <div class="doctor">
    <div class="doctor__name">Dr Alan Verity</div>
    <div class="doctor__quals">MBBS (NSW) MBiomedE FRACS (Ortho) FAOrthA</div>
    <div class="doctor__role">Orthopaedic Surgeon</div>
  </div>
  <div class="clinics">
    <div class="clinic">
      <div class="clinic__place">Ashvale</div>
      <div>12-14 Halden Road</div>
      <div>Ashvale NSW 2190</div>
      <div>Tel: 02 9000 4821</div>
      <div class="clinic__gap"></div>
      <div>Shoulder and Elbow</div>
      <div>www.verity.example.au</div>
    </div>
    <div class="clinic">
      <div class="clinic__place">Westmere</div>
      <div>88 Larkin Road</div>
      <div>Westmere NSW 2195</div>
      <div>Tel: 02 9000 7356</div>
      <div class="clinic__gap"></div>
      <div>Knee Surgery</div>
      <div>www.kneecare.example.au</div>
    </div>
  </div>
</section>

<section class="card card--details">
  <div class="brand">
    <div class="brand__mark"></div>
    <div class="brand__name">Meridale Eating</div>
  </div>
  <div class="doctor">
    <div class="doctor__name">Dr Alan Verity</div>
    <div class="doctor__quals">MBBS (NSW) MBiomedE FRACS (Ortho) FAOrthA</div>
    <div class="doctor__role">Orthopaedic Surgeon</div>
  </div>
  <div class="card__clinic card__clinic--left">
    <div class="clinic__place">Westmere</div>
    <div>Knee Surgery</div>
    <div class="clinic__gap"></div>
    <div>88 Larkin Road</div>
    <div>Westmere NSW 2195</div>
    <div><svg class="icon" viewBox="0 0 10 10"><path d="M2 1h2l1 2-1.5 1a6 6 0 0 0 2.5 2.5L7 5l2 1v2a1 1 0 0 1-1 1A8 8 0 0 1 1 2a1 1 0 0 1 1-1z" fill="#1a8fd6"/></svg> 02 9000 7356</div>
    <div><svg class="icon" viewBox="0 0 10 10"><circle cx="5" cy="5" r="4.5" fill="#6cc4ec"/></svg> www.kneecare.example.au</div>
  </div>
  <div class="card__clinic card__clinic--right">
    <div class="clinic__place">Ashvale</div>
    <div>Shoulder and Elbow</div>
    <div class="clinic__gap"></div>
    <div>12-14 Halden Road</div>
    <div>Ashvale NSW 2190</div>
    <div>02 9000 4821 <svg class="icon" viewBox="0 0 10 10"><path d="M2 1h2l1 2-1.5 1a6 6 0 0 0 2.5 2.5L7 5l2 1v2a1 1 0 0 1-1 1A8 8 0 0 1 1 2a1 1 0 0 1 1-1z" fill="#1a8fd6"/></svg></div>
    <div>www.verity.example.au <svg class="icon" viewBox="0 0 10 10"><circle cx="5" cy="5" r="4.5" fill="#6cc4ec"/></svg></div>
  </div>
  <div class="card__rule"></div>
  <div class="card__band"></div>
</section>

<section class="card card--brand">
  <div class="brand">
    <div class="brand__mark"></div>
    <div class="brand__name">Meridale Eating</div>
  </div>
</section>

</body>
</html>
```